University Entrepreneurship Housing Cohort Needs a Flyer Design

Talbot Ridge University's Venture and Discovery Center needs a flyer designed for their new "V-Loft" (short for Venture Loft) Living Learning Community.

The purpose of the V-Loft Living Learning Community (LLC) is to provide students at Talbot Ridge University with the opportunity to live, learn, and participate in activities that have an entrepreneurship and innovation focus. Students with entrepreneurial ambitions will be able to connect with others who share those similar interests and aspirations. The community will create a space for students to learn about entrepreneurial and innovative ways of thinking and working, and to begin to implement their ideas using LLC provided resources (e.g,, workshops, site visits, mentors, and peer-networking). The LLC will also include an on-site V-Loft Commons, which functions as a study space for V-Loft students. The lounge will have dry-erase walls, a 65-inch touch screen monitor, internet connectivity, and printing capabilities. The final design should communicate an exciting and innovative focused opportunity for young college students.

Note: Both logos need to be on the flyer, but pictures can be selected additionally as desired.

Target Market(s)

Undergraduate students who plan to live in on campus housing and have an interest in entrepreneurship and innovation

Industry/Entity Type

University

Font styles to use
Sans Serif

Requirements
Must have
• Both logos need to be on the flyer, but pictures can be selected additionally as desired.
• Font: Gill Sans (for larger text) and Usherwood (for smaller text)
• The purpose of the Venture Loft (V-Loft) Living Learning Community (LLC) is to provide students at Talbot Ridge University with the opportunity to live, learn, and participate in activities that have an entrepreneurship and innovation focus.
• Students with entrepreneurial ambitions will be able to connect with others who share similar interests and aspirations. Using resources provided by the V-Loft LLC and the Venture and Discovery Center, residents will begin to develop their ideas, as well as participate in experiences that include workshops, competitions, mentorship, exposure to the Atlanta ecosystem, and peer-to-peer networking.
• The V-Loft Commons will include:
• - Collaborative study space
• - Dry-erase walls
• - 65-inch touchscreen monitor
• - Internet connectivity
• - Printing capabilities
• Website: vdc.trlu.edu
• Phone: 555-286-3147
• Twitter: @TRUVDC
• Facebook: TRU_VDC
• LinkedIn: Venture & Discovery Center at Talbot Ridge University
Nice to have
• Color codes:
• Blue PMS 286
• RED PMS 186
• Grey PMS 404
• More details here: http://brandbox.trlu.edu/guidelines/visual-identity/type-color-usage/

```html
<!DOCTYPE html>
<html lang="en">
<head>
<meta charset="utf-8">
<title>V-Loft Living Learning Community Flyer</title>
<link href="https://fonts.googleapis.com/css2?family=Lato:wght@300;400&family=Fira+Sans:wght@400;600&family=Marcellus&family=Open+Sans:wght@300;400&display=swap" rel="stylesheet">
<style>
  :root {
    --brand-blue: #1e3c9c;
    --brand-blue-dark: #15307f;
    --brand-red: #c8102e;
    --brand-grey: #6b6763;
    --paper: #f2f2f2;
    --ink: #555457;
    --footer: #3a3a3c;
    --ring: #c9c9cb;
    --page-bg: #e6e6e6;
  }
  html, body {
    margin: 0;
    padding: 0;
    width: 1016px;
    height: 1200px;
    overflow: hidden;
    background: var(--page-bg);
  }
  .flyer {
    position: absolute;
    left: 68px;
    top: 31px;
    width: 850px;
    height: 1100px;
    transform: scale(1.035);
    transform-origin: top left;
    background: var(--paper);
    overflow: hidden;
    box-shadow: 0 4px 18px rgba(0,0,0,0.18);
  }
  .flyer-shapes {
    position: absolute;
    inset: 0;
  }
  .title {
    position: absolute;
    left: 0;
    width: 400px;
    top: 62px;
    text-align: center;
    margin: 0;
    font-family: "Lato", sans-serif;
    font-weight: 400;
    font-size: 88px;
    line-height: 1;
    color: #fff;
    letter-spacing: -1px;
  }
  .subtitle {
    position: absolute;
    left: 0;
    width: 386px;
    top: 165px;
    text-align: center;
    margin: 0;
    font-family: "Marcellus", serif;
    font-weight: 400;
    font-size: 35px;
    line-height: 39px;
    color: #fff;
  }
  .badge-name {
    position: absolute;
    left: 92px;
    top: 372px;
    width: 190px;
    text-align: center;
    font-family: "Lato", sans-serif;
    font-size: 38px;
    color: var(--brand-blue);
  }
  .university-name {
    position: absolute;
    left: 370px;
    top: 455px;
    width: 190px;
    text-align: right;
    font-family: "Lato", sans-serif;
    font-size: 24px;
    line-height: 27px;
    color: var(--brand-grey);
  }
  .unit-divider {
    position: absolute;
    left: 568px;
    top: 452px;
    width: 1px;
    height: 52px;
    background: var(--brand-grey);
  }
  .unit-name {
    position: absolute;
    left: 580px;
    top: 452px;
    font-family: "Lato", sans-serif;
    font-size: 21px;
    line-height: 28px;
    letter-spacing: 0.3px;
    color: var(--brand-grey);
    text-transform: uppercase;
  }
  .purpose {
    position: absolute;
    left: 66px;
    top: 528px;
    width: 742px;
    margin: 0;
    font-family: "Fira Sans", sans-serif;
    font-weight: 600;
    font-size: 19.5px;
    line-height: 25px;
    text-align: justify;
    color: var(--ink);
  }
  .commons-tab {
    position: absolute;
    left: 37px;
    top: 641px;
    width: 408px;
    height: 53px;
    box-sizing: border-box;
    padding-left: 15px;
    margin: 0;
    background: var(--brand-blue);
    border-radius: 0 12px 12px 0;
    font-family: "Fira Sans", sans-serif;
    font-weight: 600;
    font-size: 24px;
    line-height: 53px;
    color: #fff;
  }
  .amenities {
    position: absolute;
    top: 712px;
    margin: 0;
    padding: 0;
    list-style: none;
    font-family: "Open Sans", sans-serif;
    font-weight: 400;
    font-size: 23px;
    line-height: 30px;
    color: var(--ink);
  }
  .amenities--left { left: 80px; }
  .amenities--right { left: 496px; }
  .amenities li {
    position: relative;
    padding-left: 30px;
  }
  .amenities li::before {
    content: "";
    position: absolute;
    left: 0;
    top: 7px;
    width: 17px;
    height: 17px;
    border-radius: 50%;
    background: var(--ink);
  }
  .amenities li::after {
    content: "";
    position: absolute;
    left: 6px;
    top: 11px;
    border-left: 7px solid var(--paper);
    border-top: 4.5px solid transparent;
    border-bottom: 4.5px solid transparent;
  }
  .contact-main {
    position: absolute;
    left: 75px;
    right: 0;
    top: 1030px;
    text-align: center;
    font-family: "Open Sans", sans-serif;
    font-size: 26px;
    line-height: 32px;
    color: #fff;
  }
  .contact-main .contact-item {
    display: inline-flex;
    align-items: center;
    gap: 10px;
    margin: 0 8px;
  }
  .contact-social {
    position: absolute;
    left: 75px;
    right: 0;
    top: 1067px;
    text-align: center;
    font-family: "Open Sans", sans-serif;
    font-size: 14.5px;
    line-height: 20px;
    color: #dcdcdc;
  }
  .social-dot {
    display: inline-block;
    width: 8px;
    height: 8px;
    border-radius: 50%;
    background: #fff;
    margin-right: 5px;
    vertical-align: 1px;
  }
</style>
</head>
<body>
<main class="flyer">
  <svg class="flyer-shapes" width="850" height="1100" viewBox="0 0 850 1100" xmlns="http://www.w3.org/2000/svg">
    <defs>
      <linearGradient id="heroTones" x1="0" y1="0" x2="1" y2="1">
        <stop offset="0" stop-color="#c9a27a"/>
        <stop offset="0.45" stop-color="#6f5a4b"/>
        <stop offset="0.75" stop-color="#b9a63a"/>
        <stop offset="1" stop-color="#8c8a88"/>
      </linearGradient>
      <linearGradient id="studyTones" x1="0" y1="0" x2="1" y2="1">
        <stop offset="0" stop-color="#e7dccf"/>
        <stop offset="1" stop-color="#c95a5a"/>
      </linearGradient>
      <linearGradient id="atriumTones" x1="0" y1="0" x2="0" y2="1">
        <stop offset="0" stop-color="#b9c8d6"/>
        <stop offset="1" stop-color="#6c4e40"/>
      </linearGradient>
      <linearGradient id="loungeTones" x1="0" y1="0" x2="1" y2="1">
        <stop offset="0" stop-color="#8a5a4a"/>
        <stop offset="1" stop-color="#5a2a22"/>
      </linearGradient>
    </defs>

    <path role="img" aria-label="Photo of two students working together on a laptop in a dorm room"
          d="M340,0 H850 V392 C740,330 610,322 505,348 C420,370 350,405 270,425 Z" fill="url(#heroTones)"/>

    <path d="M240,428 C345,405 430,368 512,350 C625,326 755,338 850,402 V412 C752,352 625,340 515,364 C432,382 350,418 245,440 Z" fill="#fff"/>
    <path d="M245,440 C350,418 432,382 515,364 C625,340 752,352 850,412 V448 C752,390 625,378 520,396 C432,412 350,438 250,452 Z" fill="var(--brand-blue)"/>

    <path d="M0,0 H408 C408,175 345,320 215,392 L0,400 Z" fill="#5e5e60"/>
    <path d="M0,0 H396 C396,172 335,312 205,384 L0,392 Z" fill="var(--brand-blue)"/>

    <path d="M0,402 C50,404 95,410 140,424 C100,450 62,490 50,560 C40,650 38,800 42,920 C46,1000 60,1060 75,1100 H0 Z" fill="var(--brand-blue)"/>
    <path d="M140,424 C100,450 62,490 50,560 C40,650 38,800 42,920 C46,1000 60,1060 75,1100" fill="none" stroke="#fff" stroke-width="3"/>

    <circle cx="187" cy="397" r="118" fill="var(--ring)"/>
    <circle cx="187" cy="397" r="108" fill="#fff"/>

    <circle cx="225" cy="903" r="88" fill="var(--ring)"/>
    <circle role="img" aria-label="Photo of students talking in a study room" cx="225" cy="903" r="79" fill="url(#studyTones)"/>
    <circle cx="423" cy="903" r="93" fill="var(--ring)"/>
    <circle role="img" aria-label="Photo of the residence hall atrium" cx="423" cy="903" r="83" fill="url(#atriumTones)"/>
    <circle cx="627" cy="903" r="88" fill="var(--ring)"/>
    <circle role="img" aria-label="Photo of students studying on a lounge sofa" cx="627" cy="903" r="79" fill="url(#loungeTones)"/>

    <rect x="0" y="1018" width="850" height="82" fill="var(--footer)"/>
    <path d="M0,1018 H53 C56,1050 65,1078 75,1100 H0 Z" fill="var(--brand-blue)"/>
    <path d="M53,1018 C56,1050 65,1078 75,1100" fill="none" stroke="#fff" stroke-width="3"/>
  </svg>

  <h1 class="title">V-Loft</h1>
  <p class="subtitle">Living Learning<br>Community</p>

  <div class="badge-name">V-Loft</div>

  <div class="university-name">Talbot Ridge<br>University</div>
  <div class="unit-divider"></div>
  <div class="unit-name">Venture and<br>Discovery Center</div>

  <p class="purpose">The purpose of the V-Loft Living Learning Community (LLC) is to provide undergraduate students at Talbot Ridge University with the opportunity to live, learn, and participate in activities that have an entrepreneurship and innovation focus.</p>

  <h2 class="commons-tab">The V-Loft Commons Will Include</h2>

  <ul class="amenities amenities--left">
    <li>Dry-erase walls</li>
    <li>65-inch touch screen monitor</li>
    <li>Internet connectivity</li>
  </ul>
  <ul class="amenities amenities--right">
    <li>Printing capabilities</li>
    <li>Collaborative study space</li>
  </ul>

  <div class="contact-main">
    <span class="contact-item">
      <svg width="24" height="24" viewBox="0 0 24 24" aria-hidden="true">
        <circle cx="12" cy="12" r="10.5" fill="none" stroke="#fff" stroke-width="2"/>
        <path d="M8,6.5 L10,6.5 L11,9.5 L9.8,10.6 C10.5,12 11.7,13.3 13.2,14 L14.4,12.8 L17.3,13.8 L17.3,15.8 C12,16.5 7.3,11.8 8,6.5 Z" fill="#fff"/>
      </svg>
      555-286-3147
    </span>
    <span class="contact-item">
      <svg width="24" height="24" viewBox="0 0 24 24" aria-hidden="true">
        <circle cx="12" cy="12" r="10" fill="none" stroke="#fff" stroke-width="2"/>
        <ellipse cx="12" cy="12" rx="4.5" ry="10" fill="none" stroke="#fff" stroke-width="1.6"/>
        <line x1="2" y1="12" x2="22" y2="12" stroke="#fff" stroke-width="1.6"/>
      </svg>
      vdc.trlu.edu
    </span>
  </div>
  <div class="contact-social">
    <span class="social-dot"></span>TRU_VDC &bull;
    <span class="social-dot"></span>@TRUVDC &bull;
    <span class="social-dot"></span>Venture &amp; Discovery Center at Talbot Ridge University
  </div>
</main>
</body>
</html>
```